Fiscal Sponsorship Program Flyer

We are seeking a designer to create a 1-2 flyer that explains our fiscal sponsorship program. This flyer will be used to recruit new projects that might be interested in utilizing our fiscal sponsorship services. The pertinent information about our program can be found in the attached PDF. For users who cannot access the PDF, please try this link: https://files.brivanto.net/slides/d/7QtR2wXkLmZp9HvCs4YdNe8JfGaUoBi3Tx5Wl0KyRc2s/view?mode=shared

Target Market(s)

New charitable projects that do not yet have their own 501(c)(3) status, and are seeking a fiscal sponsor.

Industry/Entity Type

Nonprofit/Charity

Requirements
Must have
• The flyer must include the language and detail included on the attached PDF. The desire is to reformat this to be more appealing and easy to read.

```html
<!DOCTYPE html>
<html lang="en">
<head>
<meta charset="utf-8">
<title>Harbor Foundation – Fiscal Sponsorship Program</title>
<link href="https://fonts.googleapis.com/css2?family=Playfair+Display:ital,wght@0,400;0,600;0,700;1,400&family=Nunito+Sans:wght@400;600;700&display=swap" rel="stylesheet">
<style>
:root{
  --coral:#f25f64;
  --coral-soft:#fde3e2;
  --ink:#1d2a30;
  --text:#23282b;
  --panel:#f1f1f3;
  --backdrop:#ececee;
  --white:#ffffff;
}
*{margin:0;padding:0;box-sizing:border-box}
html,body{width:1200px;height:798px;overflow:hidden}
body{background:var(--backdrop);font-family:"Nunito Sans",Arial,sans-serif;color:var(--text);position:relative}
.page{position:absolute;top:62px;width:522px;height:675px;background:var(--white);overflow:hidden}
.page--front{left:55px}
.page--back{left:622px}
.abs{position:absolute}
.serif{font-family:"Playfair Display",Georgia,serif}
.body{font-size:9.2px;line-height:12.4px}
.h-section{font-family:"Playfair Display",Georgia,serif;color:var(--coral);font-weight:600;font-size:14.5px;line-height:17px}
.accent{color:var(--coral)}

/* front page */
.brand{left:25px;top:30px;font-family:"Playfair Display",Georgia,serif;font-weight:700;font-size:34px;line-height:33px;color:var(--ink)}
.hero-photo{left:270px;top:0;width:252px;height:118px;background:linear-gradient(135deg,#e9ebee 0%,#b9c3cf 45%,#6f7d8e 100%)}
.banner{left:0;top:118px;width:522px;height:50px;background:var(--coral);border-bottom-right-radius:48px}
.banner-title{left:25px;top:129px;font-family:"Playfair Display",Georgia,serif;font-weight:600;font-size:22px;color:var(--white)}
.front-fade{left:0;top:168px;width:522px;height:60px;background:linear-gradient(#fde8e7,rgba(255,255,255,0))}
.col-left{left:25px;top:193px;width:240px}
.col-left p{margin-bottom:10px}
.vision{font-family:"Playfair Display",Georgia,serif;font-size:10px;line-height:13.6px}
.q{font-weight:700;font-size:9.4px;line-height:12.4px;margin-bottom:5px}
.criteria{list-style:none}
.criteria li{position:relative;padding-left:12px;margin-bottom:4px}
.criteria span{position:absolute;left:0;color:var(--coral)}
.globe-photo{left:279px;top:193px;width:221px;height:193px;background:radial-gradient(circle at 55% 40%,#d7e8f1 0%,#a9c2d2 40%,#8b8073 75%,#c9bfb5 100%)}
.photo-rule{left:279px;top:386px;width:221px;height:4px;background:var(--coral)}
.philosophy{left:299px;top:402px;width:190px}
.quote{left:299px;top:456px;width:190px;border-left:1.5px solid var(--ink);padding-left:10px;font-family:"Playfair Display",Georgia,serif;font-size:11.6px;line-height:15.4px;color:var(--text)}
.philosophy-body{left:299px;top:552px;width:190px}
.foot-strip{top:660px;height:15px;background:var(--coral)}

/* back page */
.values-panel{left:0;top:0;width:251px;height:354px;background:var(--panel)}
.commit-bg{left:251px;top:0;width:271px;height:354px;background:linear-gradient(120deg,#fde9e8 0%,#ffffff 60%)}
.values{left:29px;top:22px;width:200px}
.value-name{color:var(--coral);font-weight:600;font-size:9.6px;margin-top:11px;margin-bottom:1px}
.commitments{left:281px;top:22px;width:220px}
.commit{display:flex;gap:10px;margin-top:11px}
.commit svg{flex:0 0 22px;width:22px;height:22px}
.fee-band{left:0;top:354px;width:522px;height:43px;background:var(--coral);border-top-right-radius:42px}
.fee-title{left:0;top:361px;width:522px;text-align:center;font-family:"Playfair Display",Georgia,serif;font-weight:600;font-size:20px;color:var(--white)}
.fee-fade{left:0;top:397px;width:522px;height:90px;background:linear-gradient(#fde3e2,rgba(255,255,255,0))}
.tier{top:410px;width:174px;height:255px}
.tier-divider{position:absolute;top:12px;bottom:14px;width:1px;background:#d6d6d8}
.tier-name{text-align:center;font-family:"Playfair Display",Georgia,serif;font-weight:700;font-size:17px;color:var(--ink);line-height:20px}
.tier-fee{text-align:center;font-family:"Playfair Display",Georgia,serif;font-size:10px;margin-top:2px}
.tier-kind{text-align:center;font-family:"Playfair Display",Georgia,serif;font-style:italic;font-size:12px;color:var(--coral);margin-top:10px;margin-bottom:12px}
.checks{list-style:none;padding-left:15px}
.checks li{position:relative;padding-left:11px;margin-bottom:6.5px}
.checks li::before{content:"";position:absolute;left:0;top:3px;width:6px;height:3px;border-left:1.2px solid var(--coral);border-bottom:1.2px solid var(--coral);transform:rotate(-45deg)}
.tier-lead{padding-left:12px;margin-bottom:8px}
</style>
</head>
<body>

<section class="page page--front">
  <h1 class="abs brand">Harbor<br>Foundation</h1>
  <div class="abs hero-photo" role="img" aria-label="Photo of a team joining fists over a table of papers"></div>
  <div class="abs banner"></div>
  <h2 class="abs banner-title">Fiscal Sponsorship Program</h2>
  <div class="abs front-fade"></div>

  <div class="abs col-left">
    <h3 class="h-section" style="margin-bottom:9px">Mission &amp; Vision</h3>
    <p class="body">The Harbor Foundation, founded in 2010, exists to support social impact campaigns and organizations through educational, public engagement, and awareness efforts.</p>
    <p class="vision">Its vision is to <span class="accent">strengthen</span> the capacity of the social impact sector and its leaders by providing top-tier fiscal sponsorship services.</p>
    <h3 class="h-section" style="margin-top:18px;margin-bottom:9px">What is Fiscal Sponsorship?</h3>
    <p class="q">What is fiscal sponsorship?</p>
    <p class="body" style="margin-bottom:14px">Fiscal sponsorship refers to the practice of non-profit organizations offering their legal and tax-exempt status to charitable projects or groups engaged in activities related to the sponsoring organization's mission. Fiscal sponsors provide oversight, financial management, and other administrative services to build the capacity of charitable projects.</p>
    <p class="q">What kinds of projects are eligible for fiscal sponsorship?</p>
    <p class="body" style="margin-bottom:5px">Harbor Foundation uses the following broad criteria to determine whether or not a project is eligible for fiscal sponsorship:</p>
    <ol class="criteria body">
      <li><span>1.</span>Mission alignment with the Harbor Foundation;</li>
      <li><span>2.</span>Whether or not the project provides an educational, social or charitable benefit; and</li>
      <li><span>3.</span>Whether or not the project's activities follow the IRS regulations governing 501(c)(3) public charities.</li>
    </ol>
  </div>

  <div class="abs globe-photo" role="img" aria-label="Photo of two fists bumping in front of a glowing globe"></div>
  <div class="abs photo-rule"></div>
  <h3 class="abs h-section philosophy">Fiscal Sponsorship Program Philosophy</h3>
  <blockquote class="abs quote">We believe we can <span class="accent">accelerate</span> the pace and scale of social change by providing strategic back office support to emerging projects, leaders and ideas.</blockquote>
  <p class="abs body philosophy-body">By providing light touch administrative and capacity building services, our fiscal sponsorship program takes the administrative burden off the shoulders of leaders and their projects to allow them to focus on what they do best - achieving impact and changing the world.</p>

  <div class="abs foot-strip" style="left:0;width:279px"></div>
  <div class="abs foot-strip" style="left:500px;width:22px"></div>
</section>

<section class="page page--back">
  <div class="abs values-panel"></div>
  <div class="abs commit-bg"></div>

  <div class="abs values body">
    <h3 class="h-section" style="margin-bottom:6px">Organizational Values</h3>
    <p class="value-name">Trust</p>
    <p>We believe that all successful partnerships begin with a foundation of trust.</p>
    <p class="value-name">Relationships</p>
    <p>Our partners are central to our work. We honor our relationships through respect, communication and transparency.</p>
    <p class="value-name">Embrace Complexity &amp; Risk</p>
    <p>We understand that bold solutions to intractable social issues often require both complexity and risk.</p>
    <p class="value-name" style="margin-top:14px">Innovation</p>
    <p>We embrace continuous improvement, bold creativity and change.</p>
    <p class="value-name" style="margin-top:14px">Diversity</p>
    <p>We believe that all voices matter and that effective solutions are created when decision-making is inclusive across social, cultural and economic backgrounds.</p>
  </div>

  <div class="abs commitments body">
    <h3 class="h-section" style="margin-bottom:10px">Program Commitments</h3>
    <div class="commit">
      <svg viewBox="0 0 24 24" fill="none" stroke="#f25f64" stroke-width="1.2"><path d="M3 12 21 4l-5 16-5-6-8-2z"/><path d="M21 4 11 14"/></svg>
      <p>Fast, simple and efficient fiscal sponsorship program</p>
    </div>
    <div class="commit" style="margin-top:14px">
      <svg viewBox="0 0 24 24" fill="none" stroke="#f25f64" stroke-width="1.2"><path d="M6 3h9l4 4v14H6z"/><circle cx="12.5" cy="13" r="3.5"/><path d="m11 13 1.2 1.2 2-2.2"/></svg>
      <p>Free and fast approval process - our application can be completed in 30 minutes or less. There is no fee to apply, and most projects can expect to receive a response on their application within 2 weeks</p>
    </div>
    <div class="commit" style="margin-top:14px">
      <svg viewBox="0 0 24 24" fill="none" stroke="#f25f64" stroke-width="1.2"><circle cx="11" cy="11" r="8"/><path d="M3 11h16M11 3c-3 3-3 13 0 16M11 3c3 3 3 13 0 16"/><path d="m14 19 2 2 4-4"/></svg>
      <p>No fees and no minimums; projects of any size are welcome to apply</p>
    </div>
    <div class="commit">
      <svg viewBox="0 0 24 24" fill="none" stroke="#f25f64" stroke-width="1.2"><circle cx="11" cy="11" r="8"/><path d="M3 11h16M11 3c-3 3-3 13 0 16M11 3c3 3 3 13 0 16"/><circle cx="18" cy="18" r="2.5" fill="#fff"/></svg>
      <p style="padding-top:5px">Easy onboarding process</p>
    </div>
    <div class="commit">
      <svg viewBox="0 0 24 24" fill="none" stroke="#f25f64" stroke-width="1.2"><circle cx="12" cy="6" r="3"/><path d="M7 14c2-3 8-3 10 0M2 16c3 0 5 3 9 3s7-2 11-5"/></svg>
      <p>Dedicated customer service and customization of services, tailored to the individual sponsored project's needs</p>
    </div>
    <div class="commit" style="margin-top:14px">
      <svg viewBox="0 0 24 24" fill="none" stroke="#f25f64" stroke-width="1.2"><circle cx="12" cy="12" r="3"/><circle cx="4" cy="5" r="1.5"/><circle cx="20" cy="5" r="1.5"/><circle cx="4" cy="19" r="1.5"/><circle cx="20" cy="19" r="1.5"/><path d="M5 6l5 4M19 6l-5 4M5 18l5-4M19 18l-5-4"/></svg>
      <p>Complex, hybrid structures, partnerships and coalitions are strongly encouraged to apply</p>
    </div>
  </div>

  <div class="abs fee-band"></div>
  <h2 class="abs fee-title">Fee Structure</h2>
  <div class="abs fee-fade"></div>

  <div class="abs tier body" style="left:0">
    <h3 class="tier-name">Basic</h3>
    <p class="tier-fee">Fee: 4%</p>
    <p class="tier-kind">Limited</p>
    <ul class="checks">
      <li>Project Fund Set-Up</li>
      <li>Administration &amp; Management</li>
      <li>Financial Management</li>
      <li>Grant Proposal Review</li>
      <li>Grant Contract Review</li>
      <li>Project Reporting</li>
      <li>Insurance</li>
      <li>Annual Audit and Form 990</li>
    </ul>
  </div>
  <div class="tier-divider" style="left:173px;top:472px;height:250px"></div>
  <div class="abs tier body" style="left:174px">
    <h3 class="tier-name">Standard</h3>
    <p class="tier-fee">Fee: 6%</p>
    <p class="tier-kind">Comprehensive</p>
    <p class="tier-lead">Basic Services +</p>
    <ul class="checks" style="padding-left:12px">
      <li style="margin-bottom:9px">Customized Financial Reporting</li>
      <li style="margin-bottom:9px">Monthly Financial Statements</li>
      <li style="margin-bottom:9px">Subgranting/regranting to U.S.-based organizations</li>
      <li>Management of Vendor &amp; Independent Contractors (1099s)</li>
    </ul>
  </div>
  <div class="tier-divider" style="left:347px;top:472px;height:250px"></div>
  <div class="abs tier body" style="left:348px">
    <h3 class="tier-name">Premium</h3>
    <p class="tier-fee">Fee: 10% +</p>
    <p class="tier-kind" style="margin-bottom:8px">Custom</p>
    <p class="tier-lead" style="line-height:13.6px">Standard Services +<br>custom services tailored to individual project needs.</p>
    <p class="tier-lead" style="margin-bottom:5px">Customization Options:</p>
    <ul class="checks" style="padding-left:12px">
      <li>Subgranting/regranting to international organizations</li>
      <li>Lobbying Filings</li>
      <li>Project Audit</li>
      <li>Grant Writing Assistance</li>
      <li>One-on-One Coaching</li>
    </ul>
  </div>
</section>

</body>
</html>
```